Financial Service Company Need Business Card Design

This is a new startup company, first of its kind to offer this service. We facilitate the movement of deposit funds electronically between home buyers and real estate brokerages.Our customers are DOMIVANS®, real estate brokerages, and home buyers, we identify ourselves as a financial/technology company.
Not looking for anything too flashy. Just a clean design that shows the logo, contact info, etc. Company colors can be seen on attached logo, and 'coming soon page'
www.quorvanta.ca

```html
<!DOCTYPE html>
<html lang="en">
<head>
<meta charset="utf-8">
<title>Quorvanta Business Card</title>
<link rel="stylesheet" href="https://fonts.googleapis.com/css2?family=Ubuntu:wght@400;500;700&display=swap">
<style>
  :root {
    --brand-orange: #e84e1c;
    --brand-grey: #626065;
    --text-grey: #58575b;
    --paper: #ffffff;
    --shadow: rgba(0, 0, 0, 0.22);
  }
  * { margin: 0; padding: 0; box-sizing: border-box; }
  html, body {
    width: 1200px;
    height: 402px;
    overflow: hidden;
    background: var(--paper);
    font-family: "Ubuntu", sans-serif;
  }
  .sheet { position: relative; width: 1200px; height: 402px; }

  .card {
    position: absolute;
    top: 18px;
    width: 570px;
    height: 364px;
    overflow: hidden;
    box-shadow: 5px 5px 6px var(--shadow);
  }
  .card--front { left: 18px; background: var(--paper); }
  .card--back { left: 606px; background: var(--brand-orange); }

  /* Wordmark */
  .wordmark {
    position: absolute;
    display: flex;
    align-items: center;
    gap: 22px;
    font-weight: 500;
    letter-spacing: -1px;
    line-height: 1;
  }
  .wordmark__mark { width: 58px; height: 58px; flex: none; }
  .card--front .wordmark { left: 34px; top: 64px; font-size: 66px; color: var(--brand-grey); }
  .card--front .wordmark__mark { background: var(--brand-orange); }
  .card--back .wordmark { left: 0; right: 0; top: 116px; justify-content: center; font-size: 66px; color: var(--paper); }
  .card--back .wordmark__mark { background: var(--paper); }

  .divider {
    position: absolute;
    left: 34px;
    top: 161px;
    width: 502px;
    height: 2px;
    background: var(--brand-orange);
  }

  .person { position: absolute; left: 34px; top: 196px; }
  .person__name { font-size: 27px; font-weight: 700; color: var(--brand-orange); letter-spacing: 0.2px; }
  .person__role { margin-top: 8px; font-size: 18px; font-weight: 700; color: var(--text-grey); }

  .contacts { position: absolute; left: 298px; top: 200px; list-style: none; }
  .contacts__item {
    display: flex;
    align-items: center;
    height: 30px;
    font-size: 17px;
    color: var(--text-grey);
    letter-spacing: 0.4px;
  }
  .contacts__icon { width: 22px; height: 22px; margin-right: 22px; flex: none; }

  .tagline {
    position: absolute;
    left: 0;
    right: 0;
    top: 206px;
    text-align: center;
    font-size: 22px;
    line-height: 28px;
    color: var(--paper);
  }

  .band { position: absolute; left: 0; bottom: 0; width: 570px; height: 34px; }
</style>
</head>
<body>
<main class="sheet">

  <section class="card card--front" aria-label="Business card front">
    <div class="wordmark"><span class="wordmark__mark"></span>Quorvanta</div>
    <div class="divider"></div>

    <div class="person">
      <p class="person__name">Employee Name</p>
      <p class="person__role">Position</p>
    </div>

    <ul class="contacts">
      <li class="contacts__item">
        <svg class="contacts__icon" viewBox="0 0 24 24" aria-hidden="true">
          <circle cx="12" cy="12" r="10.5" fill="none" stroke="#e84e1c" stroke-width="1.8"/>
          <path d="M8.2 6.5l1.9-.4 1.2 2.8-1.3 1.1a7 7 0 0 0 3.9 3.9l1.1-1.3 2.8 1.2-.4 1.9c-4.8.6-9.8-4.4-9.2-9.2z" fill="#e84e1c"/>
        </svg>
        1234 567 890
      </li>
      <li class="contacts__item">
        <svg class="contacts__icon" viewBox="0 0 24 24" aria-hidden="true">
          <rect x="2" y="5.5" width="20" height="13" fill="#e84e1c"/>
          <path d="M2.5 6l9.5 7.5L21.5 6" fill="none" stroke="#ffffff" stroke-width="1.6"/>
        </svg>
        @quorvanta.com
      </li>
      <li class="contacts__item">
        <svg class="contacts__icon" viewBox="0 0 24 24" aria-hidden="true">
          <g fill="none" stroke="#e84e1c" stroke-width="1.8">
            <circle cx="12" cy="12" r="10"/>
            <ellipse cx="12" cy="12" rx="4.2" ry="10"/>
            <path d="M2 12h20M3.8 6.8h16.4M3.8 17.2h16.4"/>
          </g>
        </svg>
        www.quorvanta.ca
      </li>
    </ul>

    <svg class="band" viewBox="0 0 570 34" aria-hidden="true">
      <path d="M0 0H330a6 6 0 0 1 6 5L339 34H0z" fill="#e84e1c"/>
      <path d="M349 34L352 6a6 6 0 0 1 6-6H570V34z" fill="#626065"/>
    </svg>
  </section>

  <section class="card card--back" aria-label="Business card back">
    <div class="wordmark"><span class="wordmark__mark"></span>Quorvanta</div>
    <p class="tagline">We’re changing the rules for making<br>real estate deposit transactions.</p>

    <svg class="band" viewBox="0 0 570 34" aria-hidden="true">
      <path d="M0 0H328a6 6 0 0 1 6 5L337 34H0z" fill="#626065"/>
      <path d="M347 34L350 6a6 6 0 0 1 6-6H570V34z" fill="#626065"/>
    </svg>
  </section>

</main>
</body>
</html>
```